Business Card Design

We are a flooring/granite/cabinet company
want a sleek and modern design card. Will send our logo. maybe our logo in 3d on card.
black card

Industry/Entity Type

Business

Contact Information for Business Card

Daniel Restrepo
company name Stonecrest Tile Depot
4728 loop 60w 78419
210-647-3928
stonecresttiledepot@mailbarn.net

```html
<!DOCTYPE html>
<html lang="en">
<head>
<meta charset="utf-8">
<title>Stonecrest Tile Depot – Business Card</title>
<link rel="stylesheet" href="https://fonts.googleapis.com/css2?family=Roboto:wght@400;700&display=swap">
<style>
  :root {
    --stage: #e9e7e3;
    --card: #ffffff;
    --navy: #1d3f5e;
    --ink: #1e1e1e;
    --shadow: rgba(0, 0, 0, 0.18);
  }
  * { box-sizing: border-box; margin: 0; padding: 0; }
  html, body {
    width: 1200px;
    height: 848px;
    overflow: hidden;
    background: var(--stage);
    font-family: "Roboto", Arial, sans-serif;
  }
  .stage { position: relative; width: 1200px; height: 848px; }
  .card {
    position: absolute;
    width: 540px;
    height: 309px;
    background: var(--card);
    box-shadow: 0 10px 28px var(--shadow);
  }
  .card--front { left: 60px; top: 100px; }
  .card--back { left: 600px; top: 440px; }

  .brand-name {
    font-family: "Roboto", Arial, sans-serif;
    font-weight: 700;
    color: var(--navy);
    text-transform: uppercase;
    letter-spacing: 0.04em;
    display: flex;
    align-items: center;
    gap: 12px;
    white-space: nowrap;
  }
  .brand-mark {
    width: 14px;
    height: 14px;
    background: var(--navy);
  }
  .card--front .brand-name {
    position: absolute;
    left: 0; right: 0; top: 0; bottom: 0;
    justify-content: center;
    font-size: 30px;
  }
  .card--front .brand-mark { width: 20px; height: 20px; }

  .card--back .brand-name {
    position: absolute;
    right: 34px;
    top: 42px;
    font-size: 19px;
  }
  .holder-rule {
    position: absolute;
    left: 0;
    top: 112px;
    width: 340px;
    height: 2px;
    background: var(--navy);
  }
  .holder-name {
    position: absolute;
    left: 352px;
    top: 101px;
    font-size: 17px;
    color: var(--ink);
    white-space: nowrap;
  }
  .contact-list {
    position: absolute;
    left: 34px;
    bottom: 34px;
    list-style: none;
    font-size: 16px;
    color: var(--ink);
  }
  .contact-item {
    display: flex;
    align-items: center;
    gap: 12px;
    line-height: 26px;
  }
  .contact-icon { width: 14px; height: 14px; fill: var(--ink); flex: none; }
</style>
</head>
<body>
<main class="stage">
  <section class="card card--front" aria-label="Card front">
    <div class="brand-name"><span class="brand-mark"></span>Stonecrest Tile Depot</div>
  </section>

  <section class="card card--back" aria-label="Card back">
    <div class="brand-name"><span class="brand-mark"></span>Stonecrest Tile Depot</div>
    <div class="holder-rule"></div>
    <p class="holder-name">Daniel Restrepo</p>
    <ul class="contact-list">
      <li class="contact-item">
        <svg class="contact-icon" viewBox="0 0 24 24" aria-hidden="true"><path d="M6.6 10.8a15.1 15.1 0 0 0 6.6 6.6l2.2-2.2c.3-.3.7-.4 1-.2 1.1.4 2.3.6 3.6.6.6 0 1 .4 1 1V20c0 .6-.4 1-1 1C10.6 21 3 13.4 3 4c0-.6.4-1 1-1h3.5c.6 0 1 .4 1 1 0 1.3.2 2.5.6 3.6.1.3 0 .7-.2 1z"/></svg>
        210-647-3928
      </li>
      <li class="contact-item">
        <svg class="contact-icon" viewBox="0 0 24 24" aria-hidden="true"><path d="M12 2a7 7 0 0 0-7 7c0 5.3 7 13 7 13s7-7.7 7-13a7 7 0 0 0-7-7zm0 9.5A2.5 2.5 0 1 1 12 6.5a2.5 2.5 0 0 1 0 5z"/></svg>
        4728 loop 60w 78419
      </li>
      <li class="contact-item">
        <svg class="contact-icon" viewBox="0 0 24 24" aria-hidden="true"><path d="M2 5h20v14H2zm2 2v.5l8 5 8-5V7l-8 5z"/></svg>
        stonecresttiledepot@mailbarn.net
      </li>
    </ul>
  </section>
</main>
</body>
</html>
```